Business Card Design Project

New business cards that encompass our new logo.
Looking for -
Name, Title, Cell Phone, Email, Address (2 lines), Main Phone, Fax, and website.
Reason: I don't like the graphics used to show phone, fax, cell, email, web, and address.....
I like the double sided cards with logo's on the back. I do not like the logos for phone, fax, cell, address, email, or web.

```html
<!DOCTYPE html>
<html lang="en">
<head>
<meta charset="utf-8">
<title>Northridge Supply – Business Card</title>
<link rel="stylesheet" href="https://fonts.googleapis.com/css2?family=Montserrat:ital,wght@0,400;0,700;1,400&display=swap">
<style>
  :root {
    --card-blue: #0029c4;
    --ink-white: #ffffff;
    --font-main: "Montserrat", Arial, sans-serif;
  }
  html, body {
    margin: 0;
    padding: 0;
    overflow: hidden;
    background: var(--card-blue);
  }
  .card {
    position: relative;
    width: 1200px;
    height: 667px;
    background: var(--card-blue);
    color: var(--ink-white);
    font-family: var(--font-main);
    overflow: hidden;
  }
  .brand-name {
    position: absolute;
    left: 0;
    top: 140px;
    width: 100%;
    margin: 0;
    text-align: center;
    font-size: 60px;
    font-weight: 700;
    letter-spacing: 1px;
    color: var(--ink-white);
  }
  .person {
    position: absolute;
    left: 68px;
    top: 538px;
  }
  .person-name {
    margin: 0;
    font-size: 38px;
    font-weight: 700;
    line-height: 46px;
  }
  .person-title {
    margin: 4px 0 0;
    font-size: 29px;
    font-style: italic;
    font-weight: 400;
    line-height: 36px;
  }
  .contact {
    position: absolute;
    left: 796px;
    top: 322px;
    font-size: 23px;
    font-weight: 400;
    line-height: 42px;
  }
  .contact p { margin: 0; }
  .address { margin-bottom: 12px; }
  .contact-row { display: flex; }
  .contact-label {
    width: 31px;
    font-weight: 700;
  }
  .website { margin-top: 12px; }
</style>
</head>
<body>
  <main class="card">
    <h1 class="brand-name">Northridge Supply</h1>

    <section class="person">
      <p class="person-name">Evan Marsh</p>
      <p class="person-title">Operational Manager</p>
    </section>

    <section class="contact">
      <div class="address">
        <p>1840 Harbor Lane</p>
        <p>Anchorage, AK 99501</p>
      </div>
      <p class="contact-row"><span class="contact-label">M</span><span>9412 0537</span></p>
      <p class="contact-row"><span class="contact-label">P</span><span>907 555 0148</span></p>
      <p class="contact-row"><span class="contact-label">F</span><span>907 555 0162</span></p>
      <p class="contact-row"><span class="contact-label">E</span><span>evan@northridgesupply.com</span></p>
      <p class="website">www.northridgesupply.com</p>
    </section>
  </main>
</body>
</html>
```